RESIDENTIAL CONSTRUCTION

We are a company that specializes in building custom residential homes, the design should also emphasize that quality and service is our priority.

Industry/Entity Type

Construction Company

Contact Information for Business Card

Contact Person: Tobias Kerrigan
Company Address: 243 West 9th St San Jose , Ca 95387
Phone Number : 408-736-2049
Email Address: Stonegatecrafts517@mailbrook.net

Font styles to use
Sans Serif

Colors
ec1f27

Requirements
Must have
• CSLB # 2736159
Nice to have
• needs to have same color as logo i uploaded, we will be printing these on a clear plastic card.

```html
<!DOCTYPE html>
<html lang="en">
<head>
<meta charset="utf-8">
<title>Stonegate Crafts – Business Card</title>
<link href="https://fonts.googleapis.com/css2?family=Roboto:wght@400;700&display=swap" rel="stylesheet">
<style>
  :root {
    --brand-red: #ec1f27;
    --card-white: #ffffff;
    --card-black: #1b1b1b;
    --stage: #2a2a2a;
    --ink: #555555;
    --rule: #4a4a4a;
    --silver: #a9a9a9;
  }
  * { margin: 0; padding: 0; box-sizing: border-box; }
  html, body { width: 1200px; height: 800px; overflow: hidden; }
  body {
    background: var(--stage);
    font-family: "Roboto", Arial, sans-serif;
    position: relative;
  }
  .card {
    position: absolute;
    top: 240px;
    width: 525px;
    height: 300px;
    border-radius: 3px;
  }
  .card--back { left: 45px; background: var(--card-black); }
  .card--front { left: 630px; background: var(--card-white); }

  .brand {
    display: flex;
    align-items: center;
    gap: 10px;
    font-weight: 700;
    text-transform: uppercase;
    letter-spacing: 1px;
  }
  .brand__mark { display: block; }
  .card--back .brand {
    position: absolute;
    left: 0; right: 0; top: 0; bottom: 0;
    justify-content: center;
    color: var(--silver);
    font-size: 36px;
  }
  .card--back .brand__mark { width: 30px; height: 30px; background: var(--silver); }
  .card--front .brand {
    position: absolute;
    right: 28px;
    top: 40px;
    color: var(--brand-red);
    font-size: 26px;
  }
  .card--front .brand__mark { width: 22px; height: 22px; background: var(--brand-red); }

  .divider {
    position: absolute;
    left: 28px;
    right: 28px;
    top: 140px;
    height: 1px;
    background: var(--rule);
  }
  .address {
    position: absolute;
    right: 28px;
    top: 152px;
    text-align: right;
    font-size: 13px;
    line-height: 18px;
    color: var(--ink);
  }
  .person {
    position: absolute;
    left: 28px;
    top: 196px;
    width: 240px;
  }
  .person__name {
    font-size: 17px;
    font-weight: 700;
    color: var(--brand-red);
    text-transform: uppercase;
    padding-bottom: 8px;
    border-bottom: 1px solid var(--rule);
  }
  .contact { list-style: none; margin-top: 8px; }
  .contact li {
    display: flex;
    align-items: center;
    gap: 8px;
    font-size: 13px;
    line-height: 19px;
    color: var(--ink);
  }
  .contact svg { width: 11px; height: 11px; fill: var(--brand-red); flex: none; }
</style>
</head>
<body>
  <section class="card card--back" aria-label="Card back">
    <div class="brand"><span class="brand__mark"></span>Stonegate Crafts</div>
  </section>

  <section class="card card--front" aria-label="Card front">
    <div class="brand"><span class="brand__mark"></span>Stonegate Crafts</div>
    <div class="divider"></div>
    <address class="address" style="font-style:normal">
      243 West 9th St San Jose<br>
      Ca 95387<br>
      CSLB # 2736159
    </address>
    <div class="person">
      <h1 class="person__name">Tobias Kerrigan</h1>
      <ul class="contact">
        <li>
          <svg viewBox="0 0 24 24" aria-hidden="true"><path d="M6.6 10.8a15.1 15.1 0 0 0 6.6 6.6l2.2-2.2c.3-.3.7-.4 1-.2 1.1.4 2.3.6 3.6.6.6 0 1 .4 1 1V20c0 .6-.4 1-1 1A17 17 0 0 1 3 4c0-.6.4-1 1-1h3.5c.6 0 1 .4 1 1 0 1.3.2 2.5.6 3.6.1.3 0 .7-.2 1z"/></svg>
          408-736-2049
        </li>
        <li>
          <svg viewBox="0 0 24 24" aria-hidden="true"><path d="M2 5h20v14H2z M2 5l10 8 10-8" /></svg>
          Stonegatecrafts517@mailbrook.net
        </li>
        <li>
          <svg viewBox="0 0 24 24" aria-hidden="true"><circle cx="12" cy="12" r="10"/></svg>
          www.stonegatecrafts.com
        </li>
      </ul>
    </div>
  </section>
</body>
</html>
```